Web Page Design for Major Airline Consolidator

We need a new design for an airline consolidator based out of NY. We'd really like to get the design as quickly as possible.

Here is a *very* rough mockup of what the site could look like, along with 3 main competitor's sites. Needless to say, they want a design that looks much better than their competitors. Please note that the mockup is an idea only, feel free to enhance / improve upon it.

Mockup - https://plenvora.com/trqbuild/KXMfoTzQ

Competitors:
- http://www.ruvelta.com/
- http://www.bindomark.com/home2.html
- https://www.lusopex.com/index.php
Updates

Project Deadline Extended
Reason: As per request from designers to submit additional designs.

Target Market(s)

target markets are identified in the mockup

Industry/Entity Type

Airline

Number of Pages Required

1 page

Requirements
Must have
• need space on the left side for a travel request form which is missing in the mockup. Form should have standard air booking fields (to, from, date arrival & departure, travel class, etc).

```html
<!DOCTYPE html>
<html lang="en">
<head>
<meta charset="utf-8">
<title>Brenwick Tours – Airline Consolidator</title>
<link rel="stylesheet" href="https://fonts.googleapis.com/css2?family=Oswald:wght@300;400;500&family=Lato:ital,wght@0,400;0,700;1,400;1,700&display=swap">
<style>
:root{
  --blue:#0f6fbd;
  --blue-dark:#0a5799;
  --navy:#0c2c5c;
  --orange:#ef4a23;
  --text:#4a4a4a;
  --muted:#777;
  --band:#efefef;
  --footer:#e7e7e7;
  --white:#fff;
}
*{box-sizing:border-box;margin:0;padding:0}
html,body{width:740px;height:1200px;overflow:hidden}
body{font-family:"Lato",sans-serif;color:var(--text);background:var(--white);position:relative}
.section{position:absolute;left:0;width:740px}
.abs{position:absolute}
.heading{font-family:"Oswald",sans-serif;font-weight:400;color:#444;text-align:center;font-size:14px;letter-spacing:.1px}

/* header */
.site-header{top:0;height:57px}
.brand{left:145px;top:8px;display:flex;align-items:center;gap:6px}
.brand-mark{width:18px;height:18px;border:2px solid #666;border-radius:50%}
.brand-name{font-family:"Oswald",sans-serif;font-weight:400;font-size:21px;color:#555;line-height:1}
.brand-tag{left:169px;top:36px;font-family:"Oswald",sans-serif;font-weight:300;font-size:7.5px;color:#555}
.account{left:503px;top:5px;display:flex;gap:4px}
.account a{background:var(--blue);color:#fff;font-family:"Oswald",sans-serif;font-size:7px;padding:4px 6px;border-radius:2px;text-decoration:none;display:flex;align-items:center;gap:3px}
.call{left:504px;top:27px;font-size:6.5px;color:#666;letter-spacing:.8px}

/* nav */
.main-nav{top:57px;height:20px;background:var(--blue);display:flex;justify-content:space-between;align-items:center;padding:0 147px}
.main-nav a{color:#fff;font-family:"Oswald",sans-serif;font-size:7.5px;text-decoration:none}

/* hero */
.hero{top:77px;height:190px;background:linear-gradient(180deg,#9cc3e2 0%,#c9dced 45%,#b9c3b4 62%,#7b8f58 78%,#586d33 100%)}
.hero-arrow{top:85px;width:19px;height:20px;background:var(--blue-dark);display:flex;align-items:center;justify-content:center}
.booking{left:143px;top:24px;width:181px;height:142px;background:rgba(31,120,196,.88);border:2px solid #e8f1fa;border-radius:3px;padding:6px 7px;color:#fff}
.booking h2{font-style:italic;font-weight:400;font-size:8.5px;margin-bottom:4px}
.trip{display:flex;gap:12px;font-size:6px;font-style:italic;margin-bottom:6px}
.trip span{display:flex;align-items:center;gap:3px}
.radio{width:6px;height:6px;border-radius:50%;background:#fff;border:1.5px solid #fff}
.radio.on{background:var(--blue-dark)}
.row{display:flex;align-items:center;gap:5px;margin-bottom:5px}
.field{background:#fff;color:#666;font-size:6px;font-style:italic;height:15px;display:flex;align-items:center;padding-left:4px;border-radius:1px}
.swap{width:15px;height:15px;border-radius:50%;background:#7fa0bd;display:flex;align-items:center;justify-content:center}
.date{background:#fff;color:#666;height:26px;flex:1;padding:3px 4px;font-size:6px;border-radius:1px}
.date b{display:block;font-weight:400;font-style:normal;color:#777;margin-bottom:2px}
.date i{display:flex;align-items:center;gap:3px}
.labels{display:flex;font-size:4.5px;gap:0;margin:-1px 0 1px}
.labels span:nth-child(1){width:52px}.labels span:nth-child(2){width:52px}
.counter{background:#fff;color:#555;width:47px;height:15px;display:flex;justify-content:space-between;align-items:center;padding:0 4px;font-size:7px}
.select{background:#fff;width:72px;height:15px;display:flex;align-items:center;justify-content:space-between;font-size:5.5px;color:#666;padding-left:4px}
.select span{width:13px;height:15px;background:#555;display:flex;align-items:center;justify-content:center}
.search{display:block;margin:7px auto 0;width:64px;height:18px;background:var(--orange);color:#fff;font-size:7.5px;border-radius:2px;display:flex;align-items:center;justify-content:center}
.tagline{left:412px;top:46px;width:190px;text-align:center;color:#fff;font-weight:700;font-size:10.5px;text-shadow:0 0 3px rgba(0,0,0,.25)}
.stars{left:479px;top:62px;display:flex;gap:3px}
.reviews{left:444px;top:86px;background:var(--navy);color:#fff;font-weight:700;font-size:10px;padding:2px 5px;border:1px solid #fff}
.perks{left:416px;top:88px;width:182px;height:77px;background:rgba(31,120,196,.85);border:2px solid #e8f1fa;border-radius:3px;padding:6px 10px;list-style:none;color:#fff;font-size:7.5px}
.perks li{display:flex;align-items:center;gap:5px;height:13px}

/* cards */
.agents{top:267px;height:222px}
.agents .heading{position:absolute;top:8px;width:100%}
.card{top:33px;width:144px;height:183px}
.card-head{background:var(--blue);color:#fff;text-align:center;font-family:"Oswald",sans-serif;font-size:7px;line-height:10px;height:25px;padding-top:2px}
.photo{display:block}
.card ul{list-style:none;background:#eee;font-size:5.7px;color:#666;height:43px;padding:6px 7px}
.card li{height:10px}
.card li::before,.pitch li::before{content:"» ";color:#888}
.btn{background:var(--blue);color:#fff;font-weight:700;font-size:7px;font-style:italic;display:flex;align-items:center;justify-content:center}

/* trusted */
.trusted{top:489px;height:71px;background:var(--band)}
.trusted p{left:155px;top:27px;font-family:"Oswald",sans-serif;font-weight:300;font-size:10px;color:#444}
.badge{top:11px;width:76px;height:53px;background:#fff;border:1px solid #777;display:flex;align-items:center;justify-content:center}

/* businesses */
.business{top:560px;height:164px}
.business .heading{position:absolute;top:17px;width:100%}
.pitch{left:298px;top:40px;width:300px}
.pitch h3{font-size:8px;font-weight:700;color:#444;margin-bottom:8px}
.pitch ul{list-style:none;font-size:6px;color:#666}
.pitch li{height:13px}

/* group */
.group{top:724px;height:140px;background:var(--band)}
.group .heading{position:absolute;top:8px;width:100%}
.offer h3{font-family:"Oswald",sans-serif;font-weight:400;font-size:8px;color:#444;margin-bottom:6px}
.offer p{font-size:5.6px;line-height:10px;color:#777;text-align:justify}

/* leadership */
.leader{top:864px;height:171px}
.quote{left:259px;top:16px;width:340px;font-size:6.8px;font-weight:700;line-height:11px;color:#555}
.signer{left:259px;top:42px;font-size:7.5px;font-style:italic;line-height:11px;color:#444}
.tile{top:78px;width:105px;height:77px;background:var(--blue);color:#fff;font-size:9.5px;display:flex;flex-direction:column;align-items:center;justify-content:flex-end;padding-bottom:6px;border:2px solid #dfe9f3}
.tile .circle{width:48px;height:48px;border-radius:50%;background:#fff;display:flex;align-items:center;justify-content:center;margin-bottom:6px}

/* footer */
.site-footer{top:1035px;height:137px;background:var(--footer)}
.col-title{font-size:8px;font-weight:700;color:#444}
.divider{top:16px;width:1px;height:110px;background:#d2d2d2;box-shadow:1px 0 0 #f5f5f5}
.foot-brand{left:145px;top:23px;display:flex;align-items:center;gap:4px}
.foot-brand .brand-mark{width:12px;height:12px;border-width:1.5px}
.foot-brand span{font-family:"Oswald",sans-serif;font-size:14px;color:#555}
.foot-tag{left:168px;top:40px;font-family:"Oswald",sans-serif;font-weight:300;font-size:5px;color:#555}
.contact{left:145px;font-size:6px;color:#555;display:flex;gap:6px;line-height:7.5px}
.links{left:263px;top:37px;list-style:none;font-size:5.8px;color:#555}
.links li{height:14.4px}
.links li::before{content:"»  "}
.news p{font-size:5.8px;color:#555;text-align:center;line-height:9px}
.email{width:97px;height:17px;background:#fff;border:1px solid #bbb;border-radius:3px;font-size:5.5px;font-style:italic;color:#999;padding:5px 5px}
.subscribe{width:52px;height:15px;background:#666;color:#fff;font-size:6px;font-style:italic;font-weight:700;display:flex;align-items:center;justify-content:center;border-radius:2px}
.social{left:515px;list-style:none}
.social li{display:flex;align-items:center;gap:11px;font-size:7.5px;color:#444;height:22px}
.social i{width:18px;height:18px;border:1px solid #555;border-radius:3px;background:#fff}
.copyright{top:1172px;height:28px;background:var(--blue);color:#fff;font-size:7px;display:flex;align-items:center;justify-content:center}
</style>
</head>
<body>

<header class="section site-header">
  <div class="abs brand"><span class="brand-mark"></span><span class="brand-name">Brenwick Tours</span></div>
  <div class="abs brand-tag">The Professional's choice since 1974</div>
  <div class="abs account">
    <a href="#"><svg width="6" height="6" viewBox="0 0 10 10"><circle cx="5" cy="3" r="2.5" fill="#fff"/><path d="M0 10c0-4 10-4 10 0z" fill="#fff"/></svg>My Account</a>
    <a href="#"><svg width="6" height="6" viewBox="0 0 10 10"><rect x="1" y="4" width="8" height="6" fill="#fff"/><path d="M3 4V2.5a2 2 0 0 1 4 0V4" stroke="#fff" fill="none" stroke-width="1.5"/></svg>Login</a>
  </div>
  <div class="abs call">Call Now : 1800-555-0142</div>
</header>

<nav class="section main-nav">
  <a href="#">Home</a><a href="#">Travel Agencies</a><a href="#">Religious &amp; Group Travel</a><a href="#">Corporate Concierge</a><a href="#">Niche Agencies</a><a href="#">Destinations</a><a href="#">About Brenwick</a><a href="#">Restricted Area</a>
</nav>

<section class="section hero" role="img" aria-label="Photo of a passenger jet taking off above a runway under a blue sky">
  <div class="abs hero-arrow" style="left:0"><svg width="8" height="8" viewBox="0 0 10 10"><path d="M5 1 1 5l4 4M9 1 5 5l4 4" stroke="#fff" fill="none" stroke-width="1.5"/></svg></div>
  <div class="abs hero-arrow" style="right:0"><svg width="8" height="8" viewBox="0 0 10 10"><path d="M1 1l4 4-4 4M5 1l4 4-4 4" stroke="#fff" fill="none" stroke-width="1.5"/></svg></div>

  <form class="abs booking">
    <h2>Book Flights</h2>
    <div class="trip"><span><i class="radio on"></i>Round Trip</span><span><i class="radio"></i>One Way</span></div>
    <div class="row">
      <div class="field" style="width:70px">From</div>
      <div class="swap"><svg width="8" height="8" viewBox="0 0 10 10"><path d="M1 3h7M6 1l2 2-2 2M9 7H2M4 5 2 7l2 2" stroke="#fff" fill="none" stroke-width="1.2"/></svg></div>
      <div class="field" style="flex:1">To</div>
    </div>
    <div class="row" style="gap:8px">
      <div class="date"><b>DEPARTURE</b><i><svg width="6" height="6" viewBox="0 0 10 10"><rect x="1" y="2" width="8" height="7" fill="none" stroke="#777"/><path d="M1 4h8" stroke="#777"/></svg>Select Date</i></div>
      <div class="date"><b>RETURN</b><i><svg width="6" height="6" viewBox="0 0 10 10"><rect x="1" y="2" width="8" height="7" fill="none" stroke="#777"/><path d="M1 4h8" stroke="#777"/></svg>Select Date</i></div>
    </div>
    <div class="labels"><span>ADULT (12+ YRS)</span><span>CHILD (2-11 YRS)</span><span>CLASS</span></div>
    <div class="row">
      <div class="counter"><span>-</span><span>1</span><span>+</span></div>
      <div class="counter"><span>-</span><span>0</span><span>+</span></div>
      <div class="select">Economy<span><svg width="6" height="4" viewBox="0 0 10 6"><path d="M1 1l4 4 4-4" stroke="#fff" fill="none" stroke-width="2"/></svg></span></div>
    </div>
    <div class="search">Search Flights</div>
  </form>

  <div class="abs tagline">More Than Just Airline Consolidation</div>
  <div class="abs stars">
    <svg width="60" height="10" viewBox="0 0 60 10"><g fill="#0c2c5c"><path id="s" d="M5 0l1.5 3.3 3.5.3-2.7 2.3.8 3.5L5 7.5 1.9 9.4l.8-3.5L0 3.6l3.5-.3z"/><use href="#s" x="12.5"/><use href="#s" x="25"/><use href="#s" x="37.5"/></g><path d="M55 0l1.5 3.3 3.5.3-2.7 2.3.8 3.5L55 7.5 51.9 9.4l.8-3.5L50 3.6l3.5-.3z" fill="none" stroke="#0c2c5c"/></svg>
  </div>
  <div class="abs reviews">Check Out Our Reviews!</div>
  <ul class="abs perks" style="top:128px">
    <li><svg width="7" height="7" viewBox="0 0 10 10"><rect x=".5" y=".5" width="9" height="9" fill="none" stroke="#fff"/><path d="M2 5l2 2 4-5" stroke="#fff" fill="none" stroke-width="1.4"/></svg>We're here for our clients!</li>
    <li><svg width="7" height="7" viewBox="0 0 10 10"><rect x=".5" y=".5" width="9" height="9" fill="none" stroke="#fff"/><path d="M2 5l2 2 4-5" stroke="#fff" fill="none" stroke-width="1.4"/></svg>Over 40 years in business</li>
    <li><svg width="7" height="7" viewBox="0 0 10 10"><rect x=".5" y=".5" width="9" height="9" fill="none" stroke="#fff"/><path d="M2 5l2 2 4-5" stroke="#fff" fill="none" stroke-width="1.4"/></svg>Locations across the USA</li>
    <li><svg width="7" height="7" viewBox="0 0 10 10"><rect x=".5" y=".5" width="9" height="9" fill="none" stroke="#fff"/><path d="M2 5l2 2 4-5" stroke="#fff" fill="none" stroke-width="1.4"/></svg>50+ air carriers</li>
    <li><svg width="7" height="7" viewBox="0 0 10 10"><rect x=".5" y=".5" width="9" height="9" fill="none" stroke="#fff"/><path d="M2 5l2 2 4-5" stroke="#fff" fill="none" stroke-width="1.4"/></svg>Worldwide + Europe &amp; Middle East travel</li>
  </ul>
</section>

<section class="section agents">
  <h2 class="heading">Airline Consolidator for Travel Agents</h2>
  <article class="abs card" style="left:142px">
    <div class="card-head">Home Based Travel Agents<br>Find your way to financial freedom!</div>
    <div class="photo" style="height:91px;background:linear-gradient(135deg,#dfe3e6,#b7c0c7 55%,#e8d7b8)" role="img" aria-label="Photo of a home based agent on the phone at her desk"></div>
    <ul><li>Don't lose another client to the big guys</li><li>Get more referrals and more customers!</li><li>Earn more per Month</li></ul>
    <div class="btn" style="height:24px">Join Now</div>
  </article>
  <article class="abs card" style="left:298px">
    <div class="card-head">Small Travel Agencies<br>Accelerate your growth!</div>
    <div class="photo" style="height:91px;background:linear-gradient(135deg,#6c7784,#9ba5ad 50%,#3f5a7a)" role="img" aria-label="Photo of a small agency owner working at his office desk"></div>
    <ul><li>Don't lose another client to the big guys</li><li>Get more referrals and more customers!</li><li>Earn more per Month</li></ul>
    <div class="btn" style="height:24px">Join Now</div>
  </article>
  <article class="abs card" style="left:454px">
    <div class="card-head">Corporate Travel Agencies<br>Earn &amp; retain higher value clients</div>
    <div class="photo" style="height:91px;background:linear-gradient(135deg,#f1f1f1,#c4c4c4 45%,#2e2e33)" role="img" aria-label="Photo of a corporate team meeting around a table"></div>
    <ul><li>Don't lose another client to the big guys</li><li>Get more referrals and more customers!</li><li>Earn more per Month</li></ul>
    <div class="btn" style="height:24px">Join Now</div>
  </article>
</section>

<section class="section trusted">
  <p class="abs">Trusted Members of:</p>
  <div class="abs badge" style="left:282px" aria-label="Accreditation badge"><svg width="56" height="24"><rect x="1" y="1" width="54" height="22" fill="none" stroke="#1b4f8a" stroke-width="1.5"/></svg></div>
  <div class="abs badge" style="left:392px" aria-label="Association badge"><svg width="48" height="34"><rect x="2" y="6" width="44" height="22" rx="3" fill="#e2231a"/></svg></div>
  <div class="abs badge" style="left:501px" aria-label="Industry body badge"><svg width="34" height="34"><circle cx="17" cy="17" r="15" fill="#14386b"/></svg></div>
</section>

<section class="section business">
  <h2 class="heading">Airline Consolidators for Businesses &amp; Corporations</h2>
  <div class="abs" style="left:142px;top:38px;width:143px;height:115px;border:1px solid #999;background:linear-gradient(135deg,#dde1e4,#b8bdc2 40%,#8c6a4d 80%,#c8a27f)" role="img" aria-label="Photo of a smiling call centre agent wearing a headset"></div>
  <div class="abs pitch">
    <h3>Tired of Travel Headaches? Make Business Travel EASY!</h3>
    <ul>
      <li>Excellent customer service, we staff over 200 agents and have locations in 6 major US cities.</li>
      <li>Always available ...</li>
      <li>Buy in bulk &amp; save even more!</li>
      <li>Save more by going direct to the consolidator!</li>
      <li>Your best interests are ours!</li>
    </ul>
  </div>
  <div class="abs btn" style="left:298px;top:129px;width:300px;height:24px;font-size:8px;font-style:normal">Experience the difference of Brenwick!</div>
</section>

<section class="section group">
  <h2 class="heading">Group Travel - Missionary Airfares, HAJJ &amp; Umra Discounted Airfares</h2>
  <div class="abs" style="left:142px;top:39px;width:104px;height:88px;border:1px solid #999;background:linear-gradient(180deg,#bcd3e6,#dfe6e8 55%,#d6c3a4)" role="img" aria-label="Photo of a family with luggage walking along a beach"></div>
  <div class="abs offer" style="left:259px;top:39px;width:104px">
    <h3>HAJJ Group Travel Rates</h3>
    <p>Lorem ipsum dolor sit amet, consectetur adipiscing elit. Nulla quam velit, vulputate eu pharetra nec, mattis ac neque.</p>
  </div>
  <div class="abs btn" style="left:259px;top:107px;width:104px;height:20px;font-size:7.5px;font-style:normal">Contact Us Now!</div>
  <div class="abs" style="left:377px;top:39px;width:104px;height:88px;border:1px solid #999;background:linear-gradient(135deg,#5b5a4f,#b08a6c 50%,#3a2a22)" role="img" aria-label="Photo of a volunteer holding a young child"></div>
  <div class="abs offer" style="left:494px;top:39px;width:104px">
    <h3>Missionary Travel</h3>
    <p>Lorem ipsum dolor sit amet, consectetur adipiscing elit. Nulla quam velit, vulputate eu pharetra nec, mattis ac neque.</p>
  </div>
  <div class="abs btn" style="left:494px;top:107px;width:104px;height:20px;font-size:7.5px;font-style:normal">Contact Us Now!</div>
</section>

<section class="section leader">
  <div class="abs" style="left:142px;top:12px;width:105px;height:143px;border:1px solid #999;background:linear-gradient(180deg,#f0f0f0,#d9d9d9 40%,#55585e 75%,#3d4046)" role="img" aria-label="Portrait photo of the company president in a suit"></div>
  <p class="abs quote">"Great airfares are only the beginning, exceptional customer service and caring for our clients is what makes us so unique"</p>
  <p class="abs signer">Mr. Delacourt<br>President &amp; CEO</p>
  <div class="abs tile" style="left:259px">
    <span class="circle"><svg width="22" height="22" viewBox="0 0 24 24"><rect x="2" y="4" width="17" height="16" fill="none" stroke="#1a1a1a" stroke-width="2"/><path d="M2 8h17M6 2v4M15 2v4" stroke="#1a1a1a" stroke-width="2"/><circle cx="18" cy="18" r="5" fill="var(--blue)"/></svg></span>Our History
  </div>
  <div class="abs tile" style="left:376px">
    <span class="circle"><svg width="22" height="22" viewBox="0 0 24 24" fill="#1a1a1a"><rect x="9" y="2" width="6" height="6"/><rect x="2" y="16" width="6" height="6"/><rect x="16" y="16" width="6" height="6"/><path d="M12 8v5M5 16v-3h14v3" stroke="#1a1a1a" stroke-width="2" fill="none"/></svg></span>Our Divisions
  </div>
  <div class="abs tile" style="left:493px">
    <span class="circle"><svg width="22" height="22" viewBox="0 0 24 24"><circle cx="7" cy="6" r="3" fill="#1a1a1a"/><circle cx="17" cy="6" r="3" fill="#1a1a1a"/><rect x="3" y="10" width="8" height="11" rx="2" fill="#1a1a1a"/><rect x="13" y="10" width="8" height="11" rx="2" fill="var(--blue)"/></svg></span>Our Employees
  </div>
</section>

<footer class="section site-footer">
  <div class="abs foot-brand"><span class="brand-mark"></span><span>Brenwick Tours</span></div>
  <div class="abs foot-tag">The Professional's choice since 1974</div>
  <div class="abs contact" style="top:62px"><svg width="6" height="8" viewBox="0 0 10 14"><path d="M5 0a5 5 0 0 1 5 5c0 4-5 9-5 9S0 9 0 5a5 5 0 0 1 5-5z" fill="#444"/></svg><span>618 Calder Avenue,<br>9th Floor, New York,<br>NY 10018-2204,<br>United States</span></div>
  <div class="abs contact" style="top:98px"><svg width="7" height="7" viewBox="0 0 10 10"><path d="M2 0l2 3-1 1c1 2 2 3 3 3l1-1 3 2-1 2C4 10 0 6 0 2z" fill="#444"/></svg><span>+1 212-555-0187</span></div>
  <div class="abs contact" style="top:112px"><svg width="7" height="6" viewBox="0 0 10 8"><rect width="10" height="8" fill="#444"/><path d="M0 0l5 4 5-4" stroke="#e7e7e7" fill="none"/></svg><span>info@brenwicktours.com</span></div>

  <div class="abs divider" style="left:250px"></div>
  <h3 class="abs col-title" style="left:263px;top:20px">Quick links</h3>
  <ul class="abs links"><li>Home</li><li>Travel Agencies</li><li>Religious &amp; Group Travel</li><li>Corporate Concierge</li><li>Niche Agencies</li><li>Destinations</li></ul>

  <div class="abs divider" style="left:365px"></div>
  <h3 class="abs col-title" style="left:378px;top:20px">Newslatter Singup</h3>
  <div class="abs news" style="left:378px;top:37px;width:97px"><p>Our email newsletters are a great way to get the information you're looking for<br>kestrelmail.com</p></div>
  <div class="abs email" style="left:378px;top:78px">Email Id</div>
  <div class="abs subscribe" style="left:401px;top:105px">SUBSCRIBE</div>

  <div class="abs divider" style="left:487px"></div>
  <h3 class="abs col-title" style="left:505px;top:20px">Stay Connected</h3>
  <ul class="abs social" style="top:34px"><li><i></i>Pagecircle</li><li><i></i>Chirpline</li><li><i></i>Workhub</li><li><i></i>Orbit Plus</li></ul>
</footer>

<div class="section copyright">Copyright © 2014 Brenwick Tours</div>

</body>
</html>
```